Etiketten für Nahrungsergänzung für Tiere
Zielgruppe
Wir stellen kolloidale Mischungen für Tiere her. Dies sind grob gesagt Nahrungsmittelergänzungen. Die Zielgruppe sind Tierbesitzer bzw. gesundheitsbewusste Menschen.
Aufgabenstellung
natürlich, in braun, beige, gold oder hellblau Tönen. Das Etikett wird auf eine Flasche aufgebraucht in der sich eine Flüssigkeit befindet. Das Etikett ist breiter als hoch. 115 x 61 mm (B x H)
Bisher haben wir blaue Flaschen verwendet und waren dadurch mit der Farbgebung ehr kühl und reduziert. In Zukunft wollen wir braune Flaschen mit schwarzen Deckel verwendet. Damit darf die Farbgebung auch wärmer, natürlich und das Etikett auch mit mehr Details versehen werden.
In den Uploads füge ich das aktuell Logo hinzu. Dies verwenden wir in braun/gold und in grün. Falls sich diese Gestaltung nicht so günstig auswirkt, haben wir ein 'alternative' Logo hinzugefügt. Da die Seite nächstes Jahr komplett überarbeitet wird und unsere Firma sich vergrößert, kann diese Änderung durchgeführt werden.
Ich lade noch ein Etikett hoch, welches wir für die Einzelelemente nutzen. Hier sind und bleiben die Flaschen nach wir vor blau (Herstellervorgaben), dadurch sind die Etikett sehr kühl und reduziert. Das darf auf den Entwurf für die Mischungen sehr gern deutlich verändert werden :-)

```html
<!DOCTYPE html>
<html lang="de">
<head>
<meta charset="utf-8">
<title>Silizium Etikett</title>
<link rel="stylesheet" href="https://fonts.googleapis.com/css2?family=Bebas+Neue&family=Montserrat:wght@600;700;800&family=Oswald:wght@300;400&display=swap">
<style>
  :root {
    --gold: #c09a4b;
    --gold-deep: #b08a3e;
    --gold-soft: #f3ecdf;
    --paper: #ffffff;
    --backdrop: #ded7cb;
    --ink: #2b2520;
  }
  html, body {
    margin: 0;
    padding: 0;
    width: 787px;
    height: 1200px;
    overflow: hidden;
    background: var(--backdrop);
  }
  .canvas { position: relative; width: 787px; height: 1200px; }
  .label {
    position: absolute;
    left: 23px;
    top: 404px;
    width: 740px;
    height: 392px;
    background:
      radial-gradient(ellipse 520px 420px at 330px 392px, rgba(243,236,223,0) 30%, rgba(243,236,223,0.9) 60%, rgba(255,255,255,0) 80%),
      var(--paper);
    box-shadow: 0 4px 14px rgba(0,0,0,0.12);
    overflow: hidden;
    font-family: "Montserrat", sans-serif;
  }
  .band-top {
    position: absolute;
    left: 0; top: 0;
    width: 100%;
    height: 36px;
    background: var(--gold);
    display: flex;
    justify-content: space-around;
    align-items: center;
    padding: 0 10px;
    box-sizing: border-box;
    z-index: 2;
  }
  .band-top span {
    color: var(--paper);
    font-weight: 700;
    font-size: 20px;
    letter-spacing: 1px;
  }
  .artwork {
    position: absolute;
    left: 180px;
    top: 132px;
    width: 360px;
    height: 260px;
    z-index: 0;
  }
  .artwork svg { display: block; }
  .product-name {
    position: absolute;
    left: 0;
    top: 38px;
    margin: 0;
    width: 740px;
    text-align: center;
    padding-right: 8px;
    box-sizing: border-box;
    font-weight: 800;
    font-size: 82px;
    letter-spacing: -4px;
    line-height: 1;
    color: var(--gold);
    z-index: 1;
  }
  .brand {
    position: absolute;
    left: 206px;
    top: 206px;
    display: flex;
    align-items: center;
    gap: 8px;
    font-weight: 700;
    font-size: 20px;
    color: var(--gold);
    z-index: 1;
  }
  .brand .dot {
    width: 14px; height: 14px;
    border-radius: 50%;
    background: var(--gold);
    flex: none;
  }
  .info {
    position: absolute;
    left: 430px;
    top: 138px;
    width: 184px;
    text-align: center;
    z-index: 1;
  }
  .info .kind {
    font-family: "Oswald", sans-serif;
    font-weight: 300;
    font-size: 13px;
    line-height: 1.25;
    color: var(--ink);
    text-transform: uppercase;
  }
  .info .purity {
    font-family: "Bebas Neue", sans-serif;
    font-size: 60px;
    line-height: 0.95;
    color: var(--gold);
    margin-top: 4px;
  }
  .info .claim {
    font-family: "Bebas Neue", sans-serif;
    font-size: 21px;
    line-height: 0.95;
    color: var(--gold);
    text-transform: uppercase;
    margin-top: 2px;
  }
  .info .method {
    font-size: 7.5px;
    line-height: 1.3;
    color: var(--ink);
    margin-top: 6px;
    font-weight: 600;
  }
  .side-panel {
    position: absolute;
    left: 640px;
    top: 56px;
    width: 70px;
    height: 290px;
    border: 8px solid var(--gold-soft);
    border-left: none;
    box-sizing: border-box;
    z-index: 0;
  }
  .side-text {
    position: absolute;
    left: 636px;
    top: 50px;
    width: 74px;
    height: 290px;
    z-index: 1;
  }
  .side-text .rotor {
    position: absolute;
    left: 50%;
    top: 50%;
    width: 290px;
    transform: translate(-50%, -50%) rotate(-90deg);
    text-align: center;
  }
  .side-text .storage {
    font-size: 6px;
    line-height: 1.35;
    color: var(--ink);
    font-weight: 600;
  }
  .side-text .maker {
    margin-top: 12px;
    font-size: 6px;
    font-weight: 700;
    color: var(--gold);
  }
  .band-bottom {
    position: absolute;
    left: 0; bottom: 0;
    width: 100%;
    height: 31px;
    z-index: 2;
  }
  .band-bottom svg { display: block; }
  .volume, .batch {
    position: absolute;
    bottom: 8px;
    color: var(--paper);
    font-weight: 700;
    font-size: 11px;
  }
  .volume { left: 37px; }
  .batch { left: 534px; }
</style>
</head>
<body>
<main class="canvas">
  <section class="label">
    <div class="artwork" role="img" aria-label="Goldene Linienillustration: Flamme mit konzentrischen Bögen">
      <svg width="360" height="260" viewBox="0 0 360 260" aria-hidden="true">
        <defs>
          <radialGradient id="art-glow" cx="0.5" cy="1" r="0.75">
            <stop offset="0" stop-color="#c09a4b" stop-opacity="0.55"/>
            <stop offset="0.55" stop-color="#c09a4b" stop-opacity="0.28"/>
            <stop offset="1" stop-color="#c09a4b" stop-opacity="0"/>
          </radialGradient>
          <linearGradient id="art-column" x1="0" y1="0" x2="0" y2="1">
            <stop offset="0" stop-color="#c09a4b" stop-opacity="0"/>
            <stop offset="1" stop-color="#c09a4b" stop-opacity="0.3"/>
          </linearGradient>
        </defs>
        <rect x="0" y="0" width="360" height="260" fill="url(#art-glow)"/>
        <rect x="150" y="0" width="80" height="180" rx="40" fill="url(#art-column)"/>
      </svg>
    </div>

    <div class="side-panel" aria-hidden="true"></div>

    <header class="band-top">
      <span>IONIC</span><span>IONIC</span><span>IONIC</span><span>IONIC</span>
      <span>IONIC</span><span>IONIC</span><span>IONIC</span><span>IONIC</span>
    </header>

    <h1 class="product-name">SILIZIUM</h1>

    <div class="brand"><span class="dot"></span>Aurelia</div>

    <div class="info">
      <div class="kind">Kolloid in wässriger<br>Lösunginhaltsstoffe:</div>
      <div class="purity">99,999%</div>
      <div class="claim">Reines Silizium in<br>Bidestillat</div>
      <div class="method">Kolloid aus Protonenresonanz<br>verfahren55 ppm bei Herstellung in<br>doppelt destilliertem Wasser</div>
    </div>

    <aside class="side-text">
      <div class="rotor">
        <div class="storage">Bei Raumtemperatur und lichtgeschützt lagern. Vor Mikrowellen und magnetischen Feldern fernhalten. PPM-Messmethode: Atomspektralanalyse. Anwendung nach dem Quatenprinzip der verschränkten Teilchen. Nicht für den menschlichen Verzehr</div>
        <div class="maker">Marlene Vogt, Am Lindenhang 7, 07745 Jena</div>
      </div>
    </aside>

    <footer class="band-bottom">
      <svg width="740" height="31" viewBox="0 0 740 31" aria-hidden="true">
        <polygon points="0,0 222,0 200,31 0,31" fill="var(--gold)"/>
        <polygon points="510,0 740,0 740,31 530,31" fill="var(--gold)"/>
      </svg>
      <span class="volume">30 ml/50 ml / 100 ml / 200 ml</span>
      <span class="batch">MHD-Chargen-Nr:</span>
    </footer>
  </section>
</main>
</body>
</html>
```